Electrical Contracting Business Website

Require website done for my contracting business.
Partly done one but really dont have time.

You can view the current one at http://tolbran.net.au

You can use any info/styles/photos from the current website

I like the orange color of the logo so id like things to be with that
Unfortunatly being a new business (Sept 2015) I havent got alot of photos . but if you require any for any of the specifics listed in the doc file ill have a look to see what I have.

I am targeting mainly commercial / industrial clients. Which also includes government and mining.

Target Market(s)

People requiring electricians

Industry/Entity Type

Electrician

Coding

Coded - Design and coding required

Number of Pages Required

5+ page

Colors
f37122

Requirements
Must have
• logo with EC Number
• Keep it simple and not to complicated
• Comply with the current html / style sheet standards.
• Desktop/Mobile Version compatability
Nice to have
• additional photos.
• The domestic lifts we install are by vonrim I dont have any photos of them unfortunately.
Should not have
• change colour of logo

```html
<!DOCTYPE html>
<html lang="en">
<head>
<meta charset="utf-8">
<title>Tolbran Engineering – Electrical Services</title>
<link rel="stylesheet" href="https://fonts.googleapis.com/css2?family=Open+Sans:wght@400;600;700&display=swap">
<style>
:root{
  --orange:#f37122;
  --orange-deep:#e0561a;
  --navy:#2b3544;
  --navy-dark:#222b38;
  --ink:#444;
  --grey:#8a8f96;
  --white:#fff;
}
*{box-sizing:border-box;margin:0;padding:0}
html,body{width:1200px;height:2700px;overflow:hidden}
body{font-family:"Open Sans",Arial,sans-serif;background:var(--white);color:var(--ink);position:relative}
.abs{position:absolute}

/* Hero */
.hero{left:0;top:0;width:1200px;height:795px;background:linear-gradient(100deg,#e9ebee 0%,#d6d9dc 45%,#b9bec4 70%,#8f97a0 100%)}
.hero-photo{left:540px;top:0;width:660px;height:795px;background:linear-gradient(160deg,#c9ced3 0%,#8e99a6 50%,#3f5f9c 75%,#2e4f8d 100%);opacity:.85}
.hero-panel{left:0;top:470px;width:760px;height:325px;background:linear-gradient(180deg,#5c6169 0%,#3e4349 100%);opacity:.55}
.logo{left:100px;top:34px;display:flex;align-items:center;gap:10px}
.logo-mark{width:40px;height:40px;border-radius:50%;background:var(--orange)}
.logo-name{font-weight:700;font-size:34px;color:var(--orange);letter-spacing:1px;line-height:1}
.logo-sub{font-weight:600;font-size:12px;color:var(--orange);letter-spacing:4px;display:block;margin-top:4px}
.nav{left:400px;top:44px;display:flex;gap:48px;font-size:19px;color:#555}
.nav .active{color:var(--orange)}
.hero-title{left:100px;top:230px;font-size:38px;font-weight:700;color:var(--orange)}
.hero-text{left:100px;top:290px;width:560px;font-size:17px;line-height:1.55;color:#333}
.btn{display:flex;align-items:center;gap:14px;background:var(--orange);color:var(--white);font-size:17px;padding:0 18px;height:44px}
.btn svg{width:16px;height:18px}
.hero-btn{left:100px;top:400px}

/* Welcome */
.welcome{left:0;top:795px;width:1200px;height:375px;background:var(--orange)}
.welcome-title{left:100px;width:400px;top:830px;font-size:20px;font-weight:700;color:var(--white);text-align:center}
.welcome-text{left:90px;top:882px;width:610px;font-size:15px;line-height:1.6;color:var(--white);text-align:center}
.play-btn{left:190px;top:1055px;width:270px;height:56px;background:var(--orange-deep);border:2px solid #c44a12;color:var(--white);display:flex;align-items:center;justify-content:center;gap:18px;font-size:22px}
.welcome-brand{left:720px;top:860px;font-size:66px;font-weight:700;color:rgba(255,255,255,.28);letter-spacing:2px}
.welcome-sub{left:855px;top:940px;font-size:18px;font-weight:600;color:rgba(255,255,255,.28);letter-spacing:6px}
.welcome-contact{left:830px;top:1018px;width:300px;font-size:13px;line-height:1.7;color:rgba(255,255,255,.35)}

/* Project cards */
.cards{left:0;top:1255px;width:1200px;height:395px;display:flex}
.card{flex:0 0 400px;height:395px;position:relative;color:var(--white);text-align:center;padding-top:30px}
.card-dark{background:linear-gradient(180deg,#2f3a4a 0%,#253040 100%)}
.card-mid{background:linear-gradient(180deg,#ef6a1f 0%,#d94f13 100%)}
.card-icon{display:block;margin:0 auto 6px;width:72px;height:48px}
.card h3{font-size:23px;font-weight:600;margin-bottom:14px}
.card p{width:300px;margin:0 auto;font-size:13px;line-height:1.8;text-align:left}
.card .btn{position:absolute;left:115px;top:312px;height:40px;font-size:16px}
.card-mid .btn{background:var(--navy-dark)}

/* Partners */
.partners{left:165px;top:1650px;width:870px;height:200px;display:flex;align-items:center;justify-content:space-between}
.partner{display:flex;align-items:center;gap:8px;font-size:21px;font-weight:700;color:var(--orange-deep);white-space:nowrap}
.partner i{width:26px;height:26px;border-radius:50%;background:var(--orange-deep);display:block}
.partner.dark{color:#3a3a3a}.partner.dark i{background:#3a3a3a}
.pager{width:18px;height:18px;border-radius:50%;background:#aaa;position:absolute;top:1741px}

/* Testimonial */
.testi{left:0;top:1850px;width:1200px;height:440px;background:linear-gradient(135deg,#f57b2c 0%,#f05e1c 50%,#ec5a18 100%)}
.testi-title{left:0;width:1200px;top:1893px;text-align:center;font-size:27px;color:var(--white)}
.testi-rule{left:540px;top:1940px;width:120px;height:2px;background:var(--white)}
.avatar{left:553px;top:1985px;width:94px;height:94px;border-radius:50%;background:linear-gradient(180deg,#b89a86,#5b6470);border:3px solid var(--white)}
.testi-name{left:0;width:1200px;top:2090px;text-align:center;font-size:16px;font-weight:700;color:var(--white)}
.testi-text{left:230px;width:740px;top:2130px;text-align:center;font-size:17px;line-height:1.65;color:var(--white)}
.chev{top:2000px;width:30px;height:90px}

/* Footer */
.footer{left:0;top:2400px;width:1200px;height:300px;background:var(--navy)}
.foot-logo{left:100px;top:2428px}
.foot-text{left:100px;top:2495px;width:320px;font-size:12px;line-height:1.8;color:#cfd5dc}
.foot-col{font-size:13px;color:#cfd5dc}
.foot-col h4{font-size:16px;font-weight:400;color:var(--white);margin-bottom:12px}
.menu{left:485px;top:2435px;border-left:1px solid #5a6473;padding-left:10px;height:210px}
.menu li{list-style:none;line-height:1.95}
.menu li.active{color:var(--orange)}
.address{left:620px;top:2435px;width:210px}
.address .row{display:flex;gap:10px;line-height:1.6}
.socials{display:flex;gap:22px;margin-top:30px;padding-left:30px}
.socials span{width:24px;height:24px;border-radius:50%;border:2px solid #cfd5dc;display:block}
.contact{left:862px;top:2435px;width:230px}
.field{width:228px;height:26px;background:#e6e8eb;border:1px solid #9aa2ad;margin-bottom:12px;font-size:11px;color:#777;padding:5px 8px}
.field.tall{height:48px}
.send{margin-left:182px;width:46px;height:22px;background:var(--orange);color:var(--white);font-size:11px;text-align:center;line-height:22px}
.bottom-bar{left:0;top:2670px;width:1200px;height:30px;background:var(--navy-dark);text-align:center;font-size:12px;line-height:30px;color:#cfd5dc}
</style>
</head>
<body>

<!-- Hero -->
<div class="abs hero" role="img" aria-label="Photo of an electrical switchboard with breakers and wiring"></div>
<div class="abs hero-panel" role="img" aria-label="Close-up of circuit breaker terminals"></div>
<div class="abs hero-photo" role="img" aria-label="Smiling electrician in blue overalls holding a power drill"></div>

<div class="abs logo">
  <span class="logo-mark"></span>
  <span><span class="logo-name">TOLBRAN</span><span class="logo-sub">ENGINEERING</span></span>
</div>
<nav class="abs nav">
  <span class="active">Home</span><span>About us</span><span>Residential</span><span>Commercial</span><span>Industrial</span><span>Contact us</span>
</nav>
<h1 class="abs hero-title">Specialized Electrical Services</h1>
<p class="abs hero-text">Lorem Ipsum is simply dummy text of the printing and typesetting industry. Lorem Ipsum has been the industry's standard dummy text ever since the 1500s, when an unknown printer took a galley of type and scrambled it to make</p>
<a class="abs btn hero-btn">Read More <svg viewBox="0 0 16 18"><path d="M2 1l13 8-13 8z" fill="#fff"/></svg></a>

<!-- Welcome -->
<section class="abs welcome"></section>
<h2 class="abs welcome-title">WELCOME TO TOLBRAN</h2>
<p class="abs welcome-text">Lorem Ipsum is simply dummy text of the printing and typesetting industry. Lorem Ipsum has been the industry's standard dummy text ever since the 1500s, when an unknown printer took a galley of type and scrambled it to make Lorem Ipsum is simply dummy text of the printing and typesetting industry. Lorem Ipsum has been the industry's standard dummy text ever since the 1500s, when an unknown printer took a galley of type and scrambled it to make</p>
<a class="abs play-btn"><svg width="20" height="22" viewBox="0 0 16 18"><path d="M2 1l13 8-13 8z" fill="#fff"/></svg>Play Video</a>
<div class="abs welcome-brand">TOLBRAN</div>
<div class="abs welcome-sub">ENGINEERING</div>
<div class="abs welcome-contact">Call 07 3100 4821 anytime<br>Fax 07 3100 4822 · EC 71504</div>

<!-- Project cards -->
<div class="abs cards">
  <article class="card card-dark" role="img" aria-label="Dark photo of industrial electrical work">
    <svg class="card-icon" viewBox="0 0 72 48"><g fill="none" stroke="#fff" stroke-width="3"><circle cx="22" cy="28" r="10"/><circle cx="48" cy="18" r="8"/></g></svg>
    <h3>HAVE A BIG PROJECT ?</h3>
    <p>Lorem Ipsum is simply dummy text of the printing and typesetting industry. Lorem Ipsum has been the industry's standard dummy text ever since the 1500s, when an unknown printer took a galley of type and scrambled it t</p>
    <a class="btn"><svg viewBox="0 0 16 18"><path d="M2 1l13 8-13 8z" fill="#fff"/></svg>Read more</a>
  </article>
  <article class="card card-mid" role="img" aria-label="Orange-toned photo of a control panel">
    <svg class="card-icon" viewBox="0 0 72 48"><g fill="none" stroke="#fff" stroke-width="3"><circle cx="22" cy="28" r="10"/><circle cx="48" cy="18" r="8"/></g></svg>
    <h3>HAVE A BIG PROJECT ?</h3>
    <p>Lorem Ipsum is simply dummy text of the printing and typesetting industry. Lorem Ipsum has been the industry's standard dummy text ever since the 1500s, when an unknown printer took a galley of type and scrambled it t</p>
    <a class="btn"><svg viewBox="0 0 16 18"><path d="M2 1l13 8-13 8z" fill="#fff"/></svg>Read more</a>
  </article>
  <article class="card card-dark" role="img" aria-label="Dark photo of cable installation">
    <svg class="card-icon" viewBox="0 0 72 48"><g fill="none" stroke="#fff" stroke-width="3"><circle cx="22" cy="28" r="10"/><circle cx="48" cy="18" r="8"/></g></svg>
    <h3>HAVE A BIG PROJECT ?</h3>
    <p>Lorem Ipsum is simply dummy text of the printing and typesetting industry. Lorem Ipsum has been the industry's standard dummy text ever since the 1500s, when an unknown printer took a galley of type and scrambled it t</p>
    <a class="btn"><svg viewBox="0 0 16 18"><path d="M2 1l13 8-13 8z" fill="#fff"/></svg>Read more</a>
  </article>
</div>

<!-- Partners -->
<div class="abs partners">
  <span class="partner"><i></i>SILVANE</span>
  <span class="partner dark"><i></i>Marlow Works</span>
  <span class="partner"><i></i>Copper Fern</span>
  <span class="partner"><i></i>RIDGELINE MECH</span>
  <span class="partner dark"><i></i>Halvard</span>
</div>
<span class="pager" style="left:118px"></span>
<span class="pager" style="left:1064px"></span>

<!-- Testimonial -->
<section class="abs testi" role="img" aria-label="Orange low-poly geometric background"></section>
<h2 class="abs testi-title">What Client say About</h2>
<div class="abs testi-rule"></div>
<div class="abs avatar" role="img" aria-label="Client portrait"></div>
<div class="abs testi-name">Martin Corrall</div>
<p class="abs testi-text">Lorem Ipsum is simply dummy text of the printing and typesetting industry. Lorem Ipsum has been the industry's standard dummy text ever since the 1500s, when an unknown printer took a galley of type and scrambled it t</p>
<svg class="abs chev" style="left:118px" viewBox="0 0 30 90"><path d="M26 4L6 45l20 41" fill="none" stroke="#2b3544" stroke-width="7"/></svg>
<svg class="abs chev" style="left:1052px" viewBox="0 0 30 90"><path d="M4 4l20 41-20 41" fill="none" stroke="#2b3544" stroke-width="7"/></svg>

<!-- Footer -->
<footer class="abs footer"></footer>
<div class="abs logo foot-logo">
  <span class="logo-mark" style="background:#4b5566"></span>
  <span><span class="logo-name" style="color:#5b6575;font-size:30px">TOLBRAN</span><span class="logo-sub" style="color:#5b6575">ENGINEERING</span></span>
</div>
<p class="abs foot-text">Lorem Ipsum is simply dummy text of the printing and typesetting industry. Lorem Ipsum has been the industry's standard dummy text ever since the 1500s, when an unknown printer took a galley of type and scrambled it t</p>
<div class="abs foot-col menu">
  <h4>Menu</h4>
  <ul><li class="active">Home</li><li>About us</li><li>Residential</li><li>Commercial</li><li>Industrial</li><li>Contact us</li></ul>
</div>
<div class="abs foot-col address">
  <h4>Address</h4>
  <div class="row">
    <svg width="14" height="20" viewBox="0 0 14 20"><path d="M7 0a7 7 0 0 0-7 7c0 5 7 13 7 13s7-8 7-13a7 7 0 0 0-7-7z" fill="#cfd5dc"/><circle cx="7" cy="7" r="2.5" fill="#2b3544"/></svg>
    <span>Unit 12, 88 Kestrel Road,<br>Brindale QLD 4100</span>
  </div>
  <div class="socials"><span></span><span></span><span></span><span></span></div>
</div>
<div class="abs foot-col contact">
  <h4>Contact us</h4>
  <div class="field">Name</div>
  <div class="field">Contact no</div>
  <div class="field tall">Message</div>
  <div class="send">Send</div>
</div>
<div class="abs bottom-bar">Site Map &nbsp;|&nbsp; Privacy &nbsp;|&nbsp; Term Use &nbsp;|&nbsp; ©Tolbran All right reserved.</div>

</body>
</html>
```